Harbor Crestline (Business Card Design)

Need business cards designed. Something modern, chic, and sleek. Mabye the back of the card should be the navy blue that is in the logo and then just the logo on the back.

Target Market(s)

Those in the hotel, office, and renovation industry

Contact Information for Business Card

1. Logo 2. Tomasz Ferreiro 3. CEO/Founder 4. Phone: (833) HarbCre / (833) 427-2273 5. Email: tomasz@theharborcrestline.com 6. Website: www.theharborcrestline.com

Font styles to use
Other font styles liked:
• Look at the logo font and base the font for everything else off of that.

Colors
0054AA
0677BA
7BADD7
CADEEF
E8F1F8

Requirements
Must have
• Colors that are associated in the logo
Nice to have
• Sleek modern clean and chic design.

```html
<!DOCTYPE html>
<html lang="en">
<head>
<meta charset="utf-8">
<title>Harbor Crestline Business Card</title>
<link rel="stylesheet" href="https://fonts.googleapis.com/css2?family=Montserrat:wght@500;600&family=Arimo:wght@400;700&display=swap">
<style>
  :root {
    --navy: #0e1a42;
    --gold: #c4993d;
    --paper: #f6f6f6;
    --stage: #2b2c30;
    --white: #ffffff;
  }
  * { margin: 0; padding: 0; box-sizing: border-box; }
  html, body { width: 1200px; height: 960px; overflow: hidden; }
  body {
    background: var(--stage);
    position: relative;
    font-family: "Arimo", Arial, sans-serif;
  }
  .card {
    position: absolute;
    left: 250px;
    width: 700px;
    height: 400px;
    border-radius: 22px;
    overflow: hidden;
  }
  .card--back { top: 40px; background: var(--navy); }
  .card--front { top: 520px; background: var(--navy); }

  /* back */
  .back-brand {
    position: absolute;
    left: 0; right: 0; top: 140px;
    display: flex; align-items: center; justify-content: center; gap: 18px;
    font-family: "Montserrat", sans-serif;
    font-weight: 600;
    font-size: 38px;
    letter-spacing: 4px;
    text-transform: uppercase;
    color: var(--white);
  }
  .back-brand .mark { width: 22px; height: 22px; background: var(--gold); }
  .back-url {
    position: absolute;
    right: 60px; bottom: 56px;
    font-family: "Montserrat", sans-serif;
    font-weight: 600;
    font-size: 19px;
    letter-spacing: 1px;
    color: var(--gold);
  }
  .back-url .tld { color: var(--white); font-weight: 500; }

  /* front */
  .front-top {
    position: absolute;
    left: 0; top: 0;
    width: 700px; height: 180px;
    background: var(--paper);
  }
  .front-rule {
    position: absolute;
    left: 0; top: 180px;
    width: 700px; height: 5px;
    background: var(--gold);
  }
  .front-brand {
    position: absolute;
    left: 60px; top: 56px;
    display: flex; align-items: center; gap: 14px;
    font-family: "Montserrat", sans-serif;
    font-weight: 600;
    font-size: 30px;
    line-height: 1.1;
    letter-spacing: 3px;
    text-transform: uppercase;
    color: var(--navy);
  }
  .front-brand .mark { width: 18px; height: 18px; background: var(--navy); }
  .holder {
    position: absolute;
    right: 62px; top: 212px;
    text-align: right;
  }
  .holder-name {
    font-weight: 700;
    font-size: 28px;
    color: var(--white);
    letter-spacing: 0.5px;
  }
  .holder-role {
    font-size: 18px;
    color: var(--gold);
    margin-top: 2px;
  }
  .contact {
    position: absolute;
    right: 40px; top: 292px;
    list-style: none;
    font-size: 17px;
    color: var(--white);
    text-align: right;
  }
  .contact li {
    display: flex; align-items: center; justify-content: flex-end; gap: 10px;
    line-height: 26px;
  }
  .contact svg { width: 14px; height: 14px; fill: var(--gold); flex: none; }
</style>
</head>
<body>

<section class="card card--back" aria-label="Card back">
  <div class="back-brand"><span class="mark"></span><span>Harbor Crestline</span></div>
  <p class="back-url">www.theharborcrestline<span class="tld">.com</span></p>
</section>

<section class="card card--front" aria-label="Card front">
  <div class="front-top"></div>
  <div class="front-rule"></div>

  <div class="front-brand"><span class="mark"></span><span>Harbor<br>Crestline</span></div>

  <div class="holder">
    <p class="holder-name">Tomasz Ferreiro</p>
    <p class="holder-role">CEO/Founder</p>
  </div>

  <ul class="contact">
    <li>(833) HarbCre / (833) 427-2273
      <svg viewBox="0 0 24 24"><path d="M6.6 10.8a15.1 15.1 0 0 0 6.6 6.6l2.2-2.2a1 1 0 0 1 1-.25 11.4 11.4 0 0 0 3.6.57 1 1 0 0 1 1 1V20a1 1 0 0 1-1 1A17 17 0 0 1 3 4a1 1 0 0 1 1-1h3.5a1 1 0 0 1 1 1c0 1.25.2 2.45.57 3.57a1 1 0 0 1-.25 1z"/></svg></li>
    <li>tomasz@theharborcrestline.com
      <svg viewBox="0 0 24 24"><path d="M2 5h20v14H2z M2 5l10 8 10-8" fill="var(--gold)" stroke="var(--navy)" stroke-width="1.6"/></svg></li>
    <li>www.theharborcrestline.com
      <svg viewBox="0 0 24 24"><circle cx="12" cy="12" r="10"/><path d="M2 12h20M12 2c3 3 3 17 0 20M12 2c-3 3-3 17 0 20" fill="none" stroke="var(--navy)" stroke-width="1.4"/></svg></li>
  </ul>
</section>

</body>
</html>
```